Write a tag line/slogan for an online survey company

We are about to launch a global online survey company. We have no competitors but the closest would be [url removed, login to view] I attach a simple survey to assist in understanding the website.

The survey platform we will use has unsurpassed technology at the back end that predicts human behaviour. Big companies like Brembly & Brembly pay 100's of thousand's to do one survey/model. We are bringing it to the mass market for $500 per survey/model.

We are presently considering using the tag line "world's best online survey tool"

We think the tag line can be improved. I do not like the word tool. But I am not sure, if there is anything better.

We want a tag line/slogan maximum 7 words that is global. I am going to give the money to someone - lets make it you! Lets have some fun.

```html
<!DOCTYPE html>
<html lang="en">
<head>
<meta charset="utf-8">
<title>Survey Tagline</title>
<link rel="stylesheet" href="https://fonts.googleapis.com/css2?family=Comic+Neue:wght@700&family=Cinzel:wght@900&display=swap">
<style>
  :root {
    --paper: #ffffff;
    --ink: #000000;
  }
  html, body {
    margin: 0;
    padding: 0;
    overflow: hidden;
    background: var(--paper);
  }
  .tagline-canvas {
    position: relative;
    width: 1200px;
    height: 469px;
    overflow: hidden;
    background: var(--paper);
  }
  .tagline-art {
    display: block;
    width: 1200px;
    height: 469px;
  }
  .tagline-headline {
    font-family: "Comic Neue", "Comic Sans MS", cursive;
    font-weight: 700;
    font-size: 50px;
    fill: var(--ink);
    stroke: var(--ink);
    stroke-width: 1.6px;
    stroke-linejoin: round;
  }
  .tagline-subline {
    font-family: "Cinzel", "Copperplate", serif;
    font-weight: 900;
    font-size: 21px;
    fill: var(--ink);
  }
</style>
</head>
<body>
  <main class="tagline-canvas">
    <svg class="tagline-art" viewBox="0 0 1200 469" xmlns="http://www.w3.org/2000/svg">
      <text class="tagline-headline" x="600" y="186" text-anchor="middle">Leading online surveys, because opinions matter.</text>
      <text class="tagline-subline" x="131" y="224" textLength="886" lengthAdjust="spacing">We are the best resource worldwide for all your survey needs</text>
    </svg>
  </main>
</body>
</html>
```